Come crowdsource a Web Design for a brazilian crowdsource Startup!

> NAME OF OUR STARTUP:
Mundaleo

> DESCRIPTION OF OUR STARTUP:
We are a crowdsourcing startup in Brazil providing consultancy and technology to support other companies to crowdsource their projects.
We also operate doing big crowdsource campaings related to polemic subjects in Brazil.

> WHAT ARE OUR TARGET AUDIENCE?
Our target audience are young people around 20-35 years old.
Generation Y (Millennial Generation)

> WHAT IS OUR INDUSTRY?
Internet, web

> WHAT DO WE NEED?
We need a Web Design for our first site.

We need 5 pages:
- Home
- What is Crowdsourcing?
- Solutions
- About Us
- Blog
- A box for the "Contact" tab (this is not a page)

Please, find attached a Layout Sketch of what I've imagined.

Lets talk about the sketch:
Well, first of all, it's a SKETCH, so you don't have to send proposals exactly as the sketch. The sketch is just to show how I've imagined the ditribution of the content boxes. For example, the menu bar doesnt need to be a rectangle exactly like the sketch, but, I would like to have the menu on the right side of the logo. Also, you will see that the boxes are all squeezed, of course I dont want them soo squeezed! Again, its juust a SKETCH!

About the images on the sketch:
IMG1 - Some nice and simple image related to collectivity or related to crowdsourcing or maybe use our O logo.

IMG2 - Some simple and creative image related to Consultancy. It doesnt need to be so obvious.

IMG3 - Some simple and creative image related to Web 2.0 Software Technology. It doesnt need to be so obvious.

IMG4 - Some simple and creative image related to a full package of Consultancy + Technology. It doesnt need to be so obvious.

IMG5 - Some nice and simple image related to collectivity or related to crowdsourcing.

IMG6 - Some nice and simple image related to Ideation. Maybe a light bulb? I dont know, be creative!

IMG7 - Some nice and simple image related to Crowdlabor. I dont know, be creative!

IMG8 - Some nice and simple image related to CrowdFeedback. Maybe a megaphone? A loudspeaker? I dont know, be creative!

IMG9 - Some nice and simple image related to us! Maybe our O logo ? I dont know, be creative!

THE CONTACT SIDE BAR - we need a nice and simple contact side bar. By the way, on the sketch this bar is shown only at the homepage, but when the site becomes real this bar will stay along all the pages.

THE CONTACT BOX - we need a nice and simple contact box.

ABOUT THE COLORS TO USE: we would like some color to our background and titles. We like colors similars to our logo: really light blue ? light green/blue ? light grey ? light orange ? I dont know, you guys knows more about that then me =)

CHATTERBOX SHARE/LIKE BUTTON: We would like a chatterbox share/like button somewhere on the site!

ABOUT THE ATTACHED FILES:

ADDITIONALS:
> The name Mundaleo comes from "collectivity". With our name we want to pass the idea of the collectivity from the crowdsource work model.

> Our communication is directed to the Generation Y.

> Remember, we are a Startup! So we need a modern and simple site, something like the web 2.0 trends. It must be beautiful =)

> We arent a serious company. We are a young and fun company! Please, dont come with old fashionable company sites.

> Be creative =] !

Target Market(s)

Our target audience are young people around 20-35 years old. Generation Y (Millennial Generation)

Industry/Entity Type

Communication

Requirements
Must have
• We need a Web Design for our first site.

We need 5 pages:
- Home
- What is Crowdsourcing?
- Solutions
- About Us
- Blog

ABOUT THE COLORS TO USE: we would like some color to our background and titles. We like colors similars to our logo: really light blue ? light green/blue ? light grey ? light oranges ? I dont know, you guys knows more about that then me =)

Should not have
• Poor/serious/old fashionable designs

```html
<!DOCTYPE html>
<html lang="en">
<head>
<meta charset="utf-8">
<title>Mundaleo — Crowdsourcing</title>
<link href="https://fonts.googleapis.com/css2?family=Open+Sans:wght@400;600;700&family=Varela+Round&family=Alegreya:wght@400&display=swap" rel="stylesheet">
<style>
:root{
  --teal:#2aa3b6;
  --teal-light:#6fd3e3;
  --teal-btn:#3bb3c6;
  --green:#5f9c22;
  --green-bar:#67a72b;
  --green-dark:#4e8a1a;
  --green-pale:#f1f8d2;
  --orange:#f36b1c;
  --grey-band:#e3e3e3;
  --text:#333;
  --nav:#8b8b8b;
  --white:#fff;
}
*{box-sizing:border-box;margin:0;padding:0}
html,body{width:1200px;height:1162px;overflow:hidden}
body{position:relative;font-family:"Open Sans",Arial,sans-serif;color:var(--text);
  background:linear-gradient(#f4f4f4,#eeeeee 569px,var(--grey-band) 569px,var(--grey-band) 998px,#fff 998px)}
.abs{position:absolute}
.logo{left:138px;top:36px;display:flex;align-items:center;gap:10px;font-family:"Varela Round",sans-serif;font-size:60px;color:var(--teal)}
.logo-dot{width:46px;height:46px;border-radius:50%;background:var(--teal)}
.nav{left:618px;top:47px;display:flex;align-items:center;font-size:17px}
.nav a{color:var(--nav);text-decoration:none;margin-right:28px}
.nav a.active{background:var(--teal-btn);color:#fff;font-weight:600;padding:8px 10px;border-radius:3px;margin-right:22px;box-shadow:0 2px 3px rgba(0,0,0,.15)}
.slider{left:169px;top:139px;width:861px;height:375px;border:1px solid #d6d6d6;border-radius:4px;
  background:#eef4f7;box-shadow:0 10px 12px -8px rgba(0,0,0,.35);overflow:hidden}
.slide-art{position:absolute;left:0;top:0;width:861px;height:375px;
  background:
    radial-gradient(ellipse 170px 110px at 390px 110px,rgba(247,190,60,.55),transparent 75%),
    radial-gradient(ellipse 420px 150px at 300px 270px,rgba(52,140,196,.55),transparent 80%),
    linear-gradient(#f3f7f9,#d7e7ef 60%,#c4dbe6)}
.arrow{top:309px}
.mission{left:638px;top:210px;width:360px;height:228px;border:5px solid rgba(255,255,255,.9);border-radius:4px;background:var(--teal-light);padding:14px 16px;color:#fff}
.mission h2{font-family:Arial,sans-serif;font-weight:400;font-size:38px;line-height:1.1;white-space:nowrap;margin-bottom:14px}
.mission p{font-size:15.5px;line-height:23px}
.mission b{font-weight:600}
.contact-tab{left:1156px;top:253px;width:44px;height:143px;background:var(--orange);border-radius:6px 0 0 6px}
.contact-tab span{position:absolute;left:50%;top:50%;transform:translate(-50%,-50%) rotate(-90deg);color:#fff;font-weight:700;font-size:22px;font-family:Arial,sans-serif}
.card{left:131px;top:553px;width:937px;height:402px;background:#fff;border-radius:4px;box-shadow:0 1px 4px rgba(0,0,0,.25)}
.card-head{height:60px;background:linear-gradient(#fff,#f1f1f1);border-bottom:1px solid #e5e5e5;border-radius:4px 4px 0 0}
.col{position:absolute;top:0;width:290px}
.col h3{font-family:"Alegreya",Georgia,serif;font-weight:400;color:var(--green);font-size:25px;line-height:60px;white-space:nowrap}
.photo{margin-top:23px;height:157px;border:3px solid #ececec}
.photo-a{background:radial-gradient(ellipse at 55% 60%,#c9d4de,transparent 60%),linear-gradient(135deg,#f2f6f9,#d6e3ec 60%,#b8c9d6)}
.photo-b{background:radial-gradient(ellipse at 65% 55%,#e9edf2,transparent 50%),linear-gradient(90deg,#6d5a4a,#b9c7cf 25%,#dfe6ea 60%,#8a7566)}
.photo-c{background:radial-gradient(ellipse at 55% 70%,#7d8ea6,transparent 60%),linear-gradient(135deg,#eef2f5,#c8d2dc 60%,#a9b7c6)}
.col p{margin-top:23px;font-size:14.4px;line-height:21.6px}
.more{display:inline-block;margin-top:21px;height:15px;width:77px;background:var(--teal-btn);color:#fff;font-size:10px;font-weight:600;line-height:15px;padding-left:6px;text-decoration:none;
  clip-path:polygon(0 0,88% 0,100% 50%,88% 100%,0 100%)}
.footer-bar{left:0;top:998px;width:1200px;height:63px;background:var(--green-bar);border-top:4px solid var(--green-dark);color:#fff;font-size:15px}
.fb-item{position:absolute;top:20px;display:flex;align-items:center;gap:9px}
.social-label{position:absolute;right:414px;top:22px;font-size:14px}
.socials{position:absolute;left:794px;top:22px;display:flex;gap:4px}
.socials i{display:block;width:18px;height:18px;background:#3e7fb8;border-radius:2px}
.socials i:nth-child(5){background:#f08a24}
.pill{position:absolute;top:21px;height:20px;display:flex;font-size:11px;font-weight:700;color:#333}
.pill .btn{background:linear-gradient(#fff,#dfe7ee);border:1px solid #b7c4cf;border-radius:3px;padding:0 6px;line-height:18px}
.pill .count{margin-left:4px;background:#fff;border:1px solid #ccc;font-weight:400;padding:0 4px;line-height:18px}
.newsletter{left:0;top:1061px;width:1200px;height:55px;background:var(--green-pale);font-family:Arial,Helvetica,sans-serif}
.nl-title{position:absolute;left:328px;top:9px;color:var(--green);font-weight:700;font-size:19px;line-height:20px}
.nl-sub{position:absolute;left:328px;top:31px;color:var(--green);font-size:12px;white-space:nowrap}
.nl-input{position:absolute;left:642px;top:14px;width:206px;height:28px;background:#fff;border:1px solid #c8c8c8;border-radius:4px;font-size:12px;font-style:italic;color:#777;line-height:26px;padding-left:30px}
.nl-btn{position:absolute;left:859px;top:16px;width:72px;height:25px;background:linear-gradient(#8fce2f,#5b9b16);border-radius:3px;color:#1e3306;font-weight:700;font-size:13px;text-align:center;line-height:25px}
.bottom-nav{left:142px;top:1130px;font-size:13.5px;display:flex;gap:25px}
.bottom-nav a{color:#222;text-decoration:none}
.copyright{right:142px;top:1130px;font-size:13.5px;color:#222}
</style>
</head>
<body>
<header>
  <div class="abs logo"><span class="logo-dot"></span>Mundaleo</div>
  <nav class="abs nav">
    <a class="active" href="#">What is Crowdsourcing?</a>
    <a href="#">Solutions</a>
    <a href="#">About Us</a>
    <a href="#">Blog</a>
  </nav>
</header>

<section class="abs slider">
  <div class="slide-art" role="img" aria-label="Illustration of a circle of blue figures holding hands beneath a speech bubble of colourful dots"></div>
</section>
<svg class="abs arrow" style="left:141px" width="16" height="32" viewBox="0 0 16 32"><path d="M14 2 2 16l12 14" fill="none" stroke="#333" stroke-width="2"/></svg>
<svg class="abs arrow" style="left:1043px" width="16" height="32" viewBox="0 0 16 32"><path d="M2 2l12 14L2 30" fill="none" stroke="#333" stroke-width="2"/></svg>
<div class="abs mission">
  <h2>Mundaleo Mission</h2>
  <p><b>Here we tell our mission in a few lines.</b> Lorem ipsum dolor sit amet, consectetur adipiscing elit. Vestibulum lectus ante, lacinia eu ultrices non, pellentesque at elit.</p>
</div>

<a class="abs contact-tab" href="#"><span>Contact</span></a>

<main class="abs card">
  <div class="card-head"></div>
  <article class="col" style="left:19px">
    <h3>Consultancy</h3>
    <div class="photo photo-a" role="img" aria-label="Photo of colleagues reviewing documents at an office desk"></div>
    <p>Lorem ipsum dolor sit amet, consectetur adipisicing elit, sed do eiusmod tempor incididunt ut labore et dolore magna aliqua. Ut enim ad minim veniam.</p>
    <a class="more" href="#">READ MORE</a>
  </article>
  <article class="col" style="left:324px">
    <h3>Techonlogy</h3>
    <div class="photo photo-b" role="img" aria-label="Photo of two colleagues looking at a tablet in an open office"></div>
    <p>Lorem ipsum dolor sit amet, consectetur adipisicing elit, sed do eiusmod tempor incididunt ut labore et dolore magna aliqua. Ut enim ad minim veniam.</p>
    <a class="more" href="#">READ MORE</a>
  </article>
  <article class="col" style="left:629px">
    <h3>Consultancy + Technology</h3>
    <div class="photo photo-c" role="img" aria-label="Photo of a smiling business team gathered around a laptop"></div>
    <p>Lorem ipsum dolor sit amet, consectetur adipisicing elit, sed do eiusmod tempor incididunt ut labore et dolore magna aliqua. Ut enim ad minim veniam.</p>
    <a class="more" href="#">READ MORE</a>
  </article>
</main>

<footer>
  <div class="abs footer-bar">
    <div class="fb-item" style="left:142px">
      <svg width="20" height="20" viewBox="0 0 20 20"><path d="M4 2c2 0 3 4 2 5l-1 1c1 3 3 5 6 6l1-1c1-1 5 0 5 2s-2 3-4 3C7 18 2 13 2 6c0-2 1-4 2-4z" fill="#fff"/></svg>
      <span>(555) 014-2290</span>
    </div>
    <div class="fb-item" style="left:314px">
      <svg width="19" height="13" viewBox="0 0 19 13"><rect width="19" height="13" fill="#fff"/><path d="M0 0l9.5 7L19 0" fill="none" stroke="#67a72b" stroke-width="1.5"/></svg>
      <span>hello@mundaleo.com</span>
    </div>
    <div class="social-label">Join our social networks</div>
    <div class="socials"><i></i><i></i><i></i><i></i><i></i></div>
    <div class="pill" style="left:906px"><span class="btn">Share</span><span class="count">12</span></div>
    <div class="pill" style="left:992px"><span class="btn">Like</span><span class="count">8</span></div>
  </div>

  <div class="abs newsletter">
    <svg class="abs" style="left:271px;top:8px" width="44" height="38" viewBox="0 0 44 38"><path d="M2 14 22 2l20 12v22H2z" fill="#67a72b"/><path d="M2 14l20 13 20-13" fill="none" stroke="#fff" stroke-width="2"/><rect x="12" y="10" width="20" height="3" fill="#fff"/></svg>
    <div class="nl-title">Subscribe to Our Newsletter</div>
    <div class="nl-sub">Sign up with your email to get updates fresh updates.</div>
    <div class="nl-input">enter your email address</div>
    <div class="nl-btn">Subscribe</div>
  </div>

  <nav class="abs bottom-nav">
    <a href="#">What is Crowdsourcing?</a>
    <a href="#">Solutions</a>
    <a href="#">About Us</a>
    <a href="#">Blog</a>
  </nav>
  <div class="abs copyright">© 2013 Mundaleo. All rights reserved.</div>
</footer>
</body>
</html>
```